Email Marketing Newsletter Design

Require the design of a email marketing newsletter. I will convert it into an updatable html template. I have supplied the copy for the first edition.

The newsletter is for a company that provides commercial property maintenance services such as office cleaning, lawns & gardens, electrical work etc

Web Site for client is:

http://morvelta.com.au/cgi-bin/xmlweb.cgi/home/index_html
Updates

Hi Wren

I will upload the doc as a PDF.

The width needs to be 777px

Look forward to seeing your design

Rgds
Derek

Target Market(s)

Property Facility Managers and Maintenance Managers working for commerical office buildings and large corporate sites

Industry/Entity Type

Construction

Number of Pages Required

1 page

Requirements
Must have
• Must be 777px wide
• Strong branding

• Intro paragraph

• Monthly Specials section

• Service Feature section

• Simple but clean with strong design elements
Nice to have
• Send to a friend icon

```html
<!DOCTYPE html>
<html lang="en">
<head>
<meta charset="utf-8">
<title>Morvelta Newsletter #001</title>
<link rel="stylesheet" href="https://fonts.googleapis.com/css2?family=Arimo:wght@400;700&display=swap">
<style>
:root{
  --page:#dfe0e2;
  --white:#ffffff;
  --topbar:#2a63b0;
  --navy:#0b3d7e;
  --green:#5a9a2e;
  --heading:#6a7fbe;
  --link:#1f4f9a;
  --text:#222222;
  --title:#3a3a3a;
  --muted:#6b6b6b;
  --panel:#e6e6e7;
  --rule:#c8c8c8;
  --footlink:#a9cdf2;
}
*{margin:0;padding:0;box-sizing:border-box}
html,body{width:961px;height:1200px;overflow:hidden;background:var(--page)}
body{font-family:"Arimo",Arial,sans-serif;color:var(--text)}
.stage{position:absolute;left:0;top:0;width:900px;height:1124px;transform:scale(1.0678);transform-origin:0 0}
.sheet{position:absolute;left:62px;top:0;width:776px;height:1124px;background:var(--white)}
.topbar{height:40px;background:var(--topbar);color:var(--white);font-size:11px;line-height:14px;text-align:center;padding-top:6px}
.topbar a{color:#b9d3f3;text-decoration:none}
.topbar b{color:#d9e7f8}
.masthead{position:relative;height:97px}
.masthead svg{position:absolute;left:0;top:0}
.brand{position:absolute;left:12px;top:16px;width:252px;color:var(--white)}
.brand-name{display:flex;align-items:center;gap:8px;font-size:31px;font-weight:700;letter-spacing:1px;line-height:36px;white-space:nowrap}
.brand-mark{width:30px;height:30px;background:var(--white);flex:none}
.brand-sub{font-size:14px;margin-top:4px;text-align:right}
.tagline{position:absolute;left:281px;top:24px;color:#c9d6ea;font-size:19px;white-space:nowrap}
.callline{position:absolute;left:282px;top:53px;color:var(--white);font-size:14px}
.body{display:flex;padding:23px 21px 0 16px;gap:18px}
.main{width:525px}
.side{width:196px}
.intro{display:flex;justify-content:space-between;height:187px}
.intro-text{width:320px;font-size:13.5px;line-height:18px}
.intro-text p+p{margin-top:18px;color:var(--link)}
.photo{display:block}
.photo-building{width:181px;height:169px;background:linear-gradient(160deg,#2f6fc4 0%,#6aa0de 45%,#c7d6e8 70%,#4d6a8f 100%)}
.section-head{display:flex;align-items:center;gap:6px;border-top:1px solid var(--rule);padding-top:9px;height:46px}
.section-head.plain{border-top:0;padding-top:0}
.section-head h2{font-weight:400;font-size:27px;color:var(--heading);letter-spacing:.3px}
.green-bar{height:5px;background:var(--green);margin:6px 0 22px}
.feature-title{font-size:17px;color:var(--title);font-weight:400;line-height:19px;margin-bottom:8px}
.copy{font-size:12px;line-height:18px}
.special{display:flex;gap:17px;margin-bottom:20px}
.photo-window{width:176px;height:184px;flex:none;background:linear-gradient(90deg,#7f9bb8 0%,#cfdae5 45%,#eef2f6 100%)}
.special .call{color:var(--link);font-size:14px;line-height:18px;margin-top:16px}
.photo-mop{float:left;width:176px;height:186px;margin:1px 17px 6px 0;background:linear-gradient(180deg,#c5d3de 0%,#9aa8b4 55%,#dce3e6 100%)}
.service .copy p+p{margin-top:18px}
.readmore{font-size:12px;font-weight:700;color:var(--muted);margin-top:12px}
.backtop{font-size:11px;font-weight:700;color:#8a8a8a;text-decoration:underline;margin-top:10px;display:block}
.issue-no{font-size:22px;font-weight:700;color:var(--heading)}
.issue-date{font-size:16px;color:var(--heading);margin-top:8px;text-transform:uppercase}
.panel{background:var(--panel);margin-top:18px}
.panel-head{display:flex;align-items:center;gap:8px;height:38px;padding:0 11px;border-bottom:1px solid #cfcfd1;font-size:17px;color:var(--title)}
.panel-body{padding:10px 11px 12px;font-size:12px;line-height:18px}
.panel-body b{color:var(--muted)}
.issue-list{list-style:none;padding:10px 11px}
.issue-list li{position:relative;padding-left:20px;font-size:12px;font-weight:700;color:var(--muted);line-height:18px;margin-bottom:18px}
.issue-list li:last-child{margin-bottom:0}
.issue-list li::before{content:"";position:absolute;left:2px;top:6px;width:6px;height:6px;border-radius:50%;background:var(--navy)}
.footer{position:absolute;left:0;bottom:0;width:776px;height:61px;background:var(--navy);text-align:center;color:var(--white);font-size:11px;padding-top:14px}
.footer a{color:var(--footlink);text-decoration:none}
.footer nav{margin-top:7px;font-weight:700}
.footer nav a{margin:0 4px}
</style>
</head>
<body>
<div class="stage">
 <div class="sheet">
  <div class="topbar">
   You're receiving this newsletter because you sign up at <b>www.morvelta.com.au</b><br>
   Having trouble reading this email? <a href="#">View it in your browser.</a> Not interested anymore? <a href="#">Unsubscribe Instantly.</a>
  </div>
  <header class="masthead">
   <svg width="776" height="97" viewBox="0 0 776 97">
    <path d="M0 0H776V4C560 82 250 90 0 70Z" fill="var(--navy)"/>
    <path d="M0 70C250 90 560 82 776 4V34C560 106 250 104 0 86Z" fill="var(--green)"/>
   </svg>
   <div class="brand">
    <div class="brand-name"><span class="brand-mark"></span>MORVELTA</div>
    <div class="brand-sub">Property Services Group</div>
   </div>
   <div class="tagline">Many Services, One Company, Painless Experience</div>
   <div class="callline">Call 1300 55 81 47</div>
  </header>

  <div class="body">
   <main class="main">
    <section class="intro">
     <div class="intro-text">
      <p><b>Morvelta</b> is pleased to present our first e-newsletter. We believe in making life easier for our clients. So, we have created an e-newsletter to let you know about our current promotions and the services that we offer.</p>
      <p>Please enjoy learning about the range of ways <b>Morvelta</b> can look after your office cleaning and maintenance needs.</p>
     </div>
     <div class="photo photo-building" role="img" aria-label="Modern glass office tower against a blue sky"></div>
    </section>

    <div class="section-head">
     <svg width="33" height="33" viewBox="0 0 33 33"><path d="M16.5 2L31 30H2Z" fill="#f08a1c"/><rect x="15" y="11" width="3" height="11" fill="#fff"/><rect x="15" y="24" width="3" height="3" fill="#fff"/></svg>
     <h2>MONTHLY SPECIALS</h2>
    </div>
    <div class="green-bar"></div>
    <article class="special">
     <div class="photo photo-window" role="img" aria-label="Window cleaners on a gondola against a glass facade"></div>
     <div>
      <h3 class="feature-title">December Offer: FREE Expert Morvelta Carpet and Window Clean</h3>
      <p class="copy">At Morvelta, we believe in rewarding our loyal customers. This month, we are offering a FREE carpet and window clean if you engage our standard office cleaning services for at least 6 months. There are no strings attached and no contracts to sign!</p>
      <p class="call">Call Morvelta today and allow us to manage all of your cleaning needs for you!</p>
     </div>
    </article>

    <div class="section-head plain">
     <svg width="34" height="34" viewBox="0 0 34 34"><path d="M17 1L21.6 12.2 33.5 12.9 24.3 20.5 27.3 32.2 17 25.7 6.7 32.2 9.7 20.5 0.5 12.9 12.4 12.2Z" fill="#f7a81b"/></svg>
     <h2>SERVICE FEATURE</h2>
    </div>
    <div class="green-bar"></div>
    <article class="service">
     <div class="photo-mop" role="img" aria-label="Cleaner mopping an office floor beside a yellow bucket"></div>
     <h3 class="feature-title">Morvelta Cleaning Services</h3>
     <div class="copy">
      <p>A Morvelta office clean will look after all aspects of your office site. Our service includes regularly and thoroughly cleaning: floors, desks, kitchens and bathrooms. We also look after: window cleaning, carpet cleaning, vinyl floor stripping sealing , Venetian blind cleaning, floor sweeping, floor scrubbing, high pressure cleaning, ceiling tile and light cleaning and graffiti removal.</p>
      <p>We realise that cleaning should be a background activity. You won't notice we are there; you will notice that you don't need to self manage the cleaning process, we do that for you.</p>
      <p>Allow our experienced, expert staff to project manage all of your regular, and irregular, office cleaning needs!</p>
     </div>
     <p class="readmore">Read more</p>
     <a class="backtop" href="#">Back to top</a>
    </article>
   </main>

   <aside class="side">
    <div class="issue-no"># 001</div>
    <div class="issue-date">Monday 14th Dec 2009</div>
    <div class="panel">
     <div class="panel-head">In this issue</div>
     <ul class="issue-list">
      <li>December Offer: FREE Expert Morvelta Carpet and Window Clean</li>
      <li>Morvelta Cleaning Services</li>
     </ul>
    </div>
    <div class="panel">
     <div class="panel-head">
      <svg width="24" height="22" viewBox="0 0 24 22"><path d="M0 6H11V0L24 11 11 22V16H0Z" fill="#8c8c8c"/></svg>
      Send to a friend
     </div>
     <p class="panel-body">Think you know someone that will enjoy this email? <b>Why not send it to a friend?</b></p>
    </div>
    <div class="panel">
     <div class="panel-head">
      <svg width="22" height="22" viewBox="0 0 22 22"><circle cx="11" cy="11" r="10" fill="#9a9a9a"/><circle cx="11" cy="11" r="6.5" fill="#e6e6e7"/><path d="M5 16L16 5" stroke="#9a9a9a" stroke-width="3"/></svg>
      Unsubscribe
     </div>
     <p class="panel-body">If you no longer wish to receive this mail <b>please unsubscribe.</b></p>
    </div>
   </aside>
  </div>

  <footer class="footer">
   Morvelta Property Services Group Pty Limited Unit 4, 27 Hale Street, Granville NSW 2142, Phone: 1300 55 81 47, E-mail: <a href="#">info@morvelta.com.au</a>
   <nav><a href="#">HOME</a> <a href="#">ABOUT US</a> <a href="#">DIVISIONS</a> <a href="#">ARTICLES &amp; PODCAST</a> <a href="#">LOCATIONS</a> <a href="#">INDUSTRY NEWS</a> <a href="#">CONTACT US</a></nav>
  </footer>
 </div>
</div>
</body>
</html>
```